Referral Club PostCard/ Index Card

I need to create an Index card for a Contractor Referral Club. I already did my own door hanger which I can show you. Cost is a factor because I'm just starting my company. You guys have already created my 2 logos when I did a previous logo project so I want to use those logos and colors to create a scheme double sided postcard for my referral club attached to our some examples of other ones I've seen. So, you can 1 of 3 different design/color schemes as a basis:
1) The Black background with Blue Shield
2). The Light Blue background with the white wave (Really like this and the black one)
3). My White background blue/black business card design.
So, 3 different design/color schemes to attack?

You can also look at my website for ideas

http://www.TheDwellingCounselor.example
Updates

I have a picture of the things I want to say on BOTH sides on the Index card/[Post card. Basically, there are two versions that can be created, one with the black background/blue logo motif or one with the white/blue background logo. I bought BOTH designs in my logo contest. Actually 1 is the front of the cards and the other is the back of my card. I'm looking for creativity to get these contractors to join this referral club so I can get more leads.

Need extra days to review

I have some new logos,, icons and pdfs to submit for consideration

Target Market(s)

Drawing Other Contractors into my Professional Referral Exchange Club

Industry/Entity Type

Public Insurance Adjusting

Font styles to use
Serif
Sans Serif
Other font styles liked:
• Love Zurich font but very few people have it..It is eye drawing!!

Colors
0054AA
0677BA
7BADD7
CADEEF
E8F1F8
0094D4
00A9DD
6FCCEA
C7EBF8
E9F6FB
EE7325
F08F49
F5BC92
FAE3D3
FDF4ED

Requirements
Must have
• My Blue or Black/White color scheme to stay consistent to what Ive already had done
Nice to have
• Something that jumps off to entice them to join that I haven't thought of.

```html
<!DOCTYPE html>
<html lang="en">
<head>
<meta charset="utf-8">
<title>Dwelling Counselor Referral Club Postcard</title>
<link href="https://fonts.googleapis.com/css2?family=Montserrat:wght@800;900&family=Oswald:wght@400;500;600;700&family=Tinos&family=Raleway:wght@500;700&display=swap" rel="stylesheet">
<style>
:root{
  --stage:#3b3b3b;
  --label:#6d6d6d;
  --white:#ffffff;
  --ink:#111111;
  --heading:#333333;
  --brand:#0054AA;
  --brand-deep:#0a3a9a;
  --navy:#0b2a8a;
  --sky:#0094D4;
  --sky-light:#00A9DD;
  --band:#d6d6d6;
  --alert:#ff1a25;
  --pill:#1d1d1f;
  --muted:#8a8a8a;
}
*{margin:0;padding:0;box-sizing:border-box}
html,body{width:1005px;height:1200px;overflow:hidden;background:var(--stage)}
.stage{position:relative;width:1005px;height:1200px}
.side-label{position:absolute;left:57px;font-family:"Raleway",sans-serif;font-weight:500;font-size:36px;color:var(--label);letter-spacing:1px;transform:translate(-50%,-50%) rotate(-90deg);white-space:nowrap}
.card{position:absolute;left:99px;width:802px;background:var(--white);overflow:hidden}
.card--front{top:47px;height:535px}
.card--back{top:624px;height:534px}
.abs{position:absolute}

.rating-badge{left:-90px;top:-125px;width:250px;height:250px;border-radius:50%;background:var(--alert);box-shadow:0 0 0 3px var(--white),0 0 0 5px var(--alert)}
.hero-photo{left:0;top:60px;width:305px;height:380px;background:linear-gradient(160deg,#c65a3a 0%,#f2f2f2 30%,#7a7a7a 55%,#b8bfa8 80%,#eeeeee 100%)}

.brand-mark{border-radius:50%;background:var(--brand)}
.brand-name{font-family:"Tinos",serif;color:var(--brand);text-align:center;line-height:1;white-space:nowrap}

.title-dark{font-family:"Montserrat",sans-serif;font-weight:900;color:var(--heading);line-height:1;white-space:nowrap}
.title-blue{font-family:"Montserrat",sans-serif;font-weight:900;color:var(--brand-deep);line-height:1;white-space:nowrap}
.rule{height:3px}
.rule--dark{background:var(--heading)}
.rule--blue{background:var(--brand-deep)}

.band{right:0;background:linear-gradient(90deg,rgba(214,214,214,0) 0%,var(--band) 25%)}
.bullet{width:13px;height:13px;border-radius:50%;background:var(--brand)}
.item{font-family:"Montserrat",sans-serif;font-weight:800;color:var(--ink);line-height:27px;white-space:nowrap}

.join-pill{left:289px;top:314px;width:494px;height:39px;border-radius:5px;background:linear-gradient(90deg,var(--navy),var(--brand) 50%,var(--navy));display:flex;align-items:center;justify-content:flex-end;padding-right:14px;font-family:"Oswald",sans-serif;font-weight:500;font-size:19px;color:var(--white);letter-spacing:-.3px}
.join-pill b{font-weight:700;margin-right:5px}
.award{right:28px;top:354px;font-family:"Oswald",sans-serif;font-weight:700;font-size:32px;color:var(--ink);letter-spacing:-.5px;line-height:40px;white-space:nowrap}

.footer-wave{left:0;width:802px;height:160px}
.phone-disc{left:21px;width:56px;height:56px;border-radius:50%;background:var(--white);display:flex;align-items:center;justify-content:center}
.call{left:89px;font-family:"Oswald",sans-serif;font-weight:700;font-size:45px;color:var(--white);line-height:60px;letter-spacing:-1px;white-space:nowrap}
.info-pill{left:499px;width:303px;height:33px;background:var(--pill);border-radius:6px 0 0 6px;display:flex;align-items:center;justify-content:center;color:var(--white);font-family:"Oswald",sans-serif;white-space:nowrap}

.tagline{font-family:"Raleway",sans-serif;font-weight:500;color:var(--muted);font-size:22px;white-space:nowrap}
.motto{font-family:"Montserrat",sans-serif;font-weight:800;font-style:italic;color:var(--brand);font-size:12px;letter-spacing:5px;white-space:nowrap}
</style>
</head>
<body>
<div class="stage">
  <div class="side-label" style="top:343px">FRONT PAGE</div>
  <div class="side-label" style="top:900px">BACK PAGE</div>

  <!-- Front -->
  <section class="card card--front">
    <div class="abs hero-photo" role="img" aria-label="Photo of a small model house on stacks of hundred-dollar bills"></div>
    <div class="abs rating-badge" aria-hidden="true"></div>

    <div class="abs brand-mark" style="left:268px;top:40px;width:84px;height:84px"></div>
    <div class="abs brand-name" style="left:376px;top:22px;width:390px;font-size:33px">THE DWELLING</div>
    <div class="abs brand-name" style="left:376px;top:60px;width:390px;font-size:33px">COUNSELOR</div>

    <div class="abs title-dark" style="left:467px;top:98px;font-size:41px">REFERAL</div>
    <div class="abs rule rule--dark" style="left:467px;top:143px;width:213px"></div>
    <div class="abs title-blue" style="left:375px;top:146px;font-size:43px">EXCAHNGE CLUB</div>
    <div class="abs rule rule--blue" style="left:374px;top:190px;width:397px"></div>

    <div class="abs band" style="left:300px;top:203px;height:35px"></div>
    <div class="abs band" style="left:300px;top:271px;height:35px"></div>
    <div class="abs bullet" style="left:382px;top:213px"></div>
    <div class="abs bullet" style="left:382px;top:247px"></div>
    <div class="abs bullet" style="left:382px;top:281px"></div>
    <div class="abs item" style="left:418px;top:206px;font-size:23px">EXPERT PUBLIC ADJUSTERS</div>
    <div class="abs item" style="left:418px;top:240px;font-size:23px">LOSS CONSULTANTS</div>
    <div class="abs item" style="left:418px;top:274px;font-size:23px">DAMAGE ASSESSORS</div>

    <div class="abs join-pill"><b>To join club Click:</b> network/sam whitfield/exchange a club</div>
    <div class="abs award">BEST OF THE SOUTH 8X SINCE 2010</div>

    <svg class="abs footer-wave" style="top:375px" viewBox="0 0 802 160" preserveAspectRatio="none" aria-hidden="true">
      <defs>
        <linearGradient id="waveFront" x1="0" x2="1" y1="0" y2="0">
          <stop offset="0" stop-color="#0094D4"/><stop offset="1" stop-color="#0a4fb5"/>
        </linearGradient>
      </defs>
      <path d="M0 52 C100 32 200 18 300 30 C420 48 520 74 620 70 C700 66 760 42 802 12 L802 160 L0 160Z" fill="#0b2a8a"/>
      <path d="M0 58 C120 50 220 42 330 56 C450 74 560 90 660 86 C730 83 770 72 802 58 L802 160 L0 160Z" fill="url(#waveFront)"/>
    </svg>
    <div class="abs phone-disc" style="top:461px">
      <svg width="30" height="30" viewBox="0 0 24 24" aria-hidden="true"><path fill="#0677BA" d="M6.6 10.8a15.1 15.1 0 0 0 6.6 6.6l2.2-2.2a1 1 0 0 1 1-.25 11.4 11.4 0 0 0 3.6.57 1 1 0 0 1 1 1V20a1 1 0 0 1-1 1A17 17 0 0 1 3 4a1 1 0 0 1 1-1h3.5a1 1 0 0 1 1 1c0 1.25.2 2.45.57 3.57a1 1 0 0 1-.25 1z"/></svg>
    </div>
    <div class="abs call" style="top:459px">CALL 1-800-FIXCLAIM</div>
    <div class="abs info-pill" style="top:473px;font-size:15px;font-weight:400">Serving florida, georgia, Albania and mississia</div>
  </section>

  <!-- Back -->
  <section class="card card--back">
    <div class="abs brand-mark" style="left:84px;top:50px;width:190px;height:190px"></div>
    <div class="abs brand-name" style="left:30px;top:268px;width:298px;font-size:28px">THE DWELLING</div>
    <div class="abs brand-name" style="left:30px;top:298px;width:298px;font-size:28px">COUNSELOR</div>
    <div class="abs tagline" style="left:30px;top:328px">INSURANCE CLAIM EXPERTS</div>
    <div class="abs motto" style="left:31px;top:361px">FOR THE POLICYHOLDER!!</div>

    <div class="abs title-dark" style="left:318px;top:20px;font-size:43px">TOP REASONS FOR</div>
    <div class="abs rule rule--dark" style="left:318px;top:64px;width:443px"></div>
    <div class="abs title-blue" style="left:316px;top:67px;font-size:57px">JOINING CLUB</div>
    <div class="abs rule rule--blue" style="left:316px;top:126px;width:446px"></div>

    <div class="abs band" style="left:280px;top:146px;height:65px"></div>
    <div class="abs band" style="left:330px;top:282px;height:35px"></div>
    <div class="abs bullet" style="left:363px;top:160px"></div>
    <div class="abs bullet" style="left:363px;top:227px"></div>
    <div class="abs bullet" style="left:363px;top:293px"></div>
    <div class="abs bullet" style="left:363px;top:338px"></div>
    <div class="abs item" style="left:393px;top:152px;font-size:22px">EXCLUSIVELY ONLY 1 SERVICES<br>INDUSTRY PER REGION</div>
    <div class="abs item" style="left:393px;top:219px;font-size:22px">GURANTEED RETURN REFFERAL<br>ACCOUNTABILITY</div>
    <div class="abs item" style="left:393px;top:285px;font-size:22px">$75 GIFT CARTIFICATE</div>
    <div class="abs item" style="left:393px;top:330px;font-size:22px">TRUST YOUR CLIENT HAS TAX<br>BEST LOCAL PUBLIC AJUSTERS</div>

    <svg class="abs footer-wave" style="top:385px" viewBox="0 0 802 150" preserveAspectRatio="none" aria-hidden="true">
      <defs>
        <linearGradient id="waveBack" x1="0" x2="1" y1="0" y2="0">
          <stop offset="0" stop-color="#0094D4"/><stop offset="1" stop-color="#0a4fb5"/>
        </linearGradient>
      </defs>
      <path d="M0 15 C150 40 260 55 400 50 C560 45 680 40 802 35 L802 150 L0 150Z" fill="#0b2a8a"/>
      <path d="M0 18 C150 55 260 70 400 68 C560 66 680 60 802 52 L802 150 L0 150Z" fill="url(#waveBack)"/>
    </svg>
    <div class="abs phone-disc" style="top:461px">
      <svg width="30" height="30" viewBox="0 0 24 24" aria-hidden="true"><path fill="#0677BA" d="M6.6 10.8a15.1 15.1 0 0 0 6.6 6.6l2.2-2.2a1 1 0 0 1 1-.25 11.4 11.4 0 0 0 3.6.57 1 1 0 0 1 1 1V20a1 1 0 0 1-1 1A17 17 0 0 1 3 4a1 1 0 0 1 1-1h3.5a1 1 0 0 1 1 1c0 1.25.2 2.45.57 3.57a1 1 0 0 1-.25 1z"/></svg>
    </div>
    <div class="abs call" style="top:459px">CALL 1-800-FIXCLAIM</div>
    <div class="abs info-pill" style="top:473px;font-size:17px;font-weight:600;letter-spacing:2px">CONSULTANCY POLICY &amp; CLAIM</div>
  </section>
</div>
</body>
</html>
```